Business Card Design

Semi retired Estate Agent opening new small business. I am not chasing or wanting to sell everyday houses.. I quite like land and development sales or special projects
..Will need letterheads design and electronic header for electronic mail.
Would like the wording of "Where experience counts".Envisage simple design..max 3 colours..have strong belief in red , white and blue colours on white background

Would think that the words "Neil Harcombe" be bigger than the words "Real Estate"
I don't want it too busy as many cards are..also has to be classy..!!!
Bold card with my name and mobile number and "Where Experience Counts" on the main side and the details on the reverse.
But I am open to suggestions.!!!!!

Target Market(s)

Possible other real estate agents in Western Australia..semi commercial clients.

Industry/Entity Type

Electronic

Contact Information for Business Card

Neil Harcombe Real Estate

Neil Harcombe
Principal and Licensee
neil@neilharcombere.com.au
mobile 0427581934
ph/f 08 96172385 4B Wattlebank Pde,Claremont ,WA,6010

Requirements
Must have
• I do like the term Where Experience Counts"..The reverse side to have address etc..the face side to have name and m obile number

```html
<!DOCTYPE html>
<html lang="en">
<head>
<meta charset="utf-8">
<title>Neil Harcombe Real Estate – Business Card</title>
<link href="https://fonts.googleapis.com/css2?family=Open+Sans:wght@300;400;600&display=swap" rel="stylesheet">
<style>
  :root {
    --red-bright: #e0222a;
    --red-mid: #b81a22;
    --red-deep: #6e0c11;
    --white: #ffffff;
    --backdrop: #ece9e4;
    --shadow: rgba(60, 30, 20, 0.25);
  }
  * { margin: 0; padding: 0; box-sizing: border-box; }
  html, body {
    width: 1200px; height: 1000px; overflow: hidden;
    background: var(--backdrop);
    font-family: "Open Sans", Arial, sans-serif;
  }
  .card {
    position: absolute;
    width: 700px; height: 400px;
    box-shadow: 0 10px 30px var(--shadow);
    overflow: hidden;
  }

  /* Reverse side */
  .card--reverse { left: 360px; top: 60px; background: var(--white); }
  .reverse__band {
    position: absolute; left: 0; top: 44px; width: 100%; height: 92px;
    background: linear-gradient(to bottom, var(--red-deep) 0%, var(--red-mid) 55%, var(--red-bright) 100%);
    display: flex; align-items: center; justify-content: center; gap: 18px;
    color: var(--white);
  }
  .reverse__name { font-size: 27px; font-weight: 400; letter-spacing: 1.5px; }
  .reverse__title { font-size: 16px; font-weight: 400; letter-spacing: 1px; margin-top: -10px; }
  .reverse__details {
    position: absolute; left: 0; top: 168px; width: 100%;
    list-style: none; text-align: center;
    color: var(--red-bright); font-size: 21px; letter-spacing: 1px; line-height: 42px;
  }
  .reverse__details li { display: flex; align-items: center; justify-content: center; gap: 10px; }
  .icon { width: 20px; height: 20px; fill: none; stroke: var(--red-bright); stroke-width: 1.6; }
  .icon--solid { fill: var(--red-bright); stroke: none; }

  /* Face side */
  .card--face {
    left: 160px; top: 520px;
    background: var(--white);
  }
  .face__field {
    position: absolute; left: 0; top: 0; width: 100%; height: 318px;
    background: radial-gradient(ellipse 70% 85% at 55% 62%, var(--red-bright) 0%, var(--red-mid) 45%, var(--red-deep) 100%);
  }
  .face__name {
    position: absolute; left: 66px; top: 70px;
    color: var(--white); font-size: 50px; font-weight: 400; letter-spacing: 1px; line-height: 1;
  }
  .face__trade {
    position: absolute; left: 64px; top: 134px;
    color: var(--white); font-size: 24px; font-weight: 300; letter-spacing: 2.5px; text-transform: uppercase;
  }
  .face__tagline {
    position: absolute; right: 22px; bottom: 24px;
    color: var(--red-bright); font-size: 29px; font-weight: 400; letter-spacing: 2.5px;
  }
</style>
</head>
<body>

<section class="card card--reverse" aria-label="Business card reverse side">
  <div class="reverse__band">
    <span class="reverse__name">Neil Harcombe</span>
    <span class="reverse__title">Principal</span>
  </div>
  <ul class="reverse__details">
    <li>
      <svg class="icon icon--solid" viewBox="0 0 20 20" aria-hidden="true"><path d="M5 2l3 3-2 2.5c1 2.3 2.7 4 5 5L13.5 10l3 3-2 3c-6 0-11.5-5.5-11.5-11.5z"/></svg>
      <span>0427 581 934</span>
    </li>
    <li>
      <svg class="icon" viewBox="0 0 20 20" aria-hidden="true"><rect x="5" y="2" width="10" height="6"/><rect x="2" y="8" width="16" height="8"/><rect x="5" y="13" width="10" height="5"/></svg>
      <span>08 96172385</span>
    </li>
    <li>
      <svg class="icon" viewBox="0 0 20 20" aria-hidden="true"><rect x="2" y="4" width="16" height="12"/><path d="M2 4l8 7 8-7"/></svg>
      <span>neil@neilharcombere.com.au</span>
    </li>
    <li><span>4B Wattlebank Pde, Marlow Heights, WA, 6091.</span></li>
  </ul>
</section>

<section class="card card--face" aria-label="Business card face side">
  <div class="face__field">
    <h1 class="face__name">Neil Harcombe</h1>
    <p class="face__trade">Real Estate</p>
  </div>
  <p class="face__tagline">Where Experience Counts</p>
</section>

</body>
</html>
```